Energy Drink Brands Packaging Design

I require design for a startup energy drink, This will be the design that will be printed on the cans.

Name
482

Brief
Must think disruptive, 482 is the beasts number so I would want the eyes of satan/devil incorporated within the design however the design must be clean, and not too busy most of the attention must be given to the name and the beasts eyes. I have attached image of a major energy drink , I would like to use a similar layout and colour scheme whilst incorporating my own branding statements
Updates

Reason: I have extended the deadline as there are some very strong designs coming through.

Target Market(s)

All energy drink lovers, males, females etc

Industry/Entity Type

Startup

Font styles to use
Sans Serif

Colors
0255a3
f3f1f8

Requirements
Must have
• Similar colour layout to the major energy Drink brand we all know KV
Nice to have
• I would like to see different concepts of a satanic/beast eyes whilst giving it a sleek and attractive look

```html
<!DOCTYPE html>
<html lang="en">
<head>
<meta charset="utf-8">
<title>482 Energy Drink – Can Label</title>
<link rel="stylesheet" href="https://fonts.googleapis.com/css2?family=Lato:wght@300;400;700&display=swap">
<style>
  :root {
    --backdrop: #560609;
    --backdrop-deep: #3a0204;
    --label-maroon: #5a1b1f;
    --brand-maroon: #4a1418;
    --label-white: #f3f1f8;
    --label-black: #1b1a1b;
    --ink-soft: #e9e4e6;
    --ink-grey: #c9c6c9;
    --ink-dark: #2a1a1c;
  }
  html, body {
    margin: 0;
    padding: 0;
    width: 1200px;
    height: 1200px;
    overflow: hidden;
  }
  body {
    background: radial-gradient(ellipse at 50% 60%, var(--backdrop) 0%, var(--backdrop-deep) 100%);
    display: flex;
    align-items: center;
    justify-content: center;
    font-family: "Lato", sans-serif;
  }
  .can-label {
    width: 440px;
    height: 1021px;
    display: block;
    box-shadow: 0 20px 60px rgba(0,0,0,0.35);
  }
  .panel-maroon { fill: var(--label-maroon); }
  .panel-white { fill: var(--label-white); }
  .panel-black { fill: var(--label-black); }
  .serving-note {
    fill: var(--ink-soft);
    font-family: "Lato", sans-serif;
    font-weight: 300;
    font-size: 11px;
  }
  .brand-name {
    fill: var(--brand-maroon);
    font-family: "Lato", sans-serif;
    font-weight: 700;
    font-size: 104px;
    letter-spacing: 1px;
  }
  .product-type {
    fill: var(--ink-dark);
    font-family: "Lato", sans-serif;
    font-weight: 400;
    font-size: 22px;
  }
  .volume {
    fill: var(--ink-grey);
    font-family: "Lato", sans-serif;
    font-weight: 300;
    font-size: 9px;
  }
</style>
</head>
<body>
  <svg class="can-label" viewBox="0 0 250 580" xmlns="http://www.w3.org/2000/svg" role="group" aria-label="482 Energy Drink can label">
    <defs>
      <radialGradient id="mascot-tone" cx="0.5" cy="0.4" r="0.6">
        <stop offset="0" stop-color="#7a3a3e" stop-opacity="0.45"/>
        <stop offset="1" stop-color="#5a1b1f" stop-opacity="0.15"/>
      </radialGradient>
    </defs>

    <rect class="panel-maroon" x="0" y="0" width="250" height="580"/>
    <rect class="panel-black" x="0" y="440" width="250" height="140"/>

    <path class="panel-white label-swoosh"
          d="M250,55 C238,92 210,112 150,122 L150,500 C195,480 232,455 250,422 Z"/>
    <ellipse class="panel-white" cx="132" cy="305" rx="130" ry="200"/>

    <text class="serving-note" x="27" y="75">Slightly Carbonated.</text>
    <text class="serving-note" x="27" y="92">Serve Chilled.</text>

    <text class="brand-name" x="130" y="245" text-anchor="middle">482</text>

    <ellipse class="mascot-area" role="img" aria-label="Illustration of a grinning devil's face with glowing red eyes"
             fill="url(#mascot-tone)" cx="130" cy="370" rx="92" ry="125"/>

    <text class="product-type" x="130" y="448" text-anchor="middle">ENERGY DRINK</text>

    <text class="volume" x="232" y="562" text-anchor="end">8.4 FL OZ (250ML)</text>
  </svg>
</body>
</html>
```